Cups in Quiet Bloom webdesign + shopvantix implementation

Hi there!
We are a brand new small company located in central Europe, specializing in handmade coffee and tea mugs - please check www.cupsinquietbloom.example

We are looking for a complete redesign, something easy, nothing complicated.

1. web desing (smooth and easy - homepage,product detail page, etc...)
2. html/css
3. shopvantix platform implementation

Industry/Entity Type

It Company

```html
<!DOCTYPE html>
<html lang="en">
<head>
<meta charset="utf-8">
<title>Cups in Quiet Bloom</title>
<link rel="stylesheet" href="https://fonts.googleapis.com/css2?family=Source+Sans+3:ital,wght@0,400;0,600;0,700;1,400&display=swap">
<style>
:root{
  --cream:#f3efe2;
  --cream-card:#f6f3ea;
  --brown-dark:#3a2219;
  --brown-band:#4a2c22;
  --brown-btn:#4b2c1b;
  --brown-text:#5a3a22;
  --wood-light:#6a4428;
  --wood-mid:#573520;
  --wood-deep:#44281a;
  --bottom-bar:#2e1a10;
  --wall:#75716e;
  --mat:#c2a987;
  --text:#4a4a4a;
  --muted:#6b6b6b;
  --white:#ffffff;
}
*{box-sizing:border-box;margin:0;padding:0}
html,body{width:1200px;height:2757px;overflow:hidden}
body{position:relative;background:var(--white);font-family:"Source Sans 3",sans-serif;color:var(--text)}
.abs{position:absolute}

.site-header{left:0;top:0;width:1200px;height:132px;background:var(--cream);border-top:6px solid var(--brown-dark)}
.brand{left:40px;top:0;width:282px;height:166px;background:var(--cream);border-radius:0 0 22px 22px;box-shadow:0 3px 6px rgba(0,0,0,.35);z-index:3;display:flex;align-items:center;justify-content:center;flex-direction:column;gap:12px}
.brand-mark{width:22px;height:22px;background:var(--brown-text)}
.brand-name{font-size:26px;font-weight:600;color:var(--brown-dark)}
.util-nav{right:58px;top:16px;font-size:15px;color:var(--muted);display:flex}
.util-nav span{padding:0 10px;border-left:1px solid #b9b2a2}
.util-nav span:first-child{border-left:0}
.main-nav{right:44px;top:90px;display:flex;font-size:18px;font-weight:700;color:var(--brown-text);text-transform:uppercase}
.main-nav span{padding:0 16px;border-left:1px solid #b9a88c}
.main-nav span:first-child{border-left:0}

.hero-band{left:0;top:132px;width:1200px;height:533px;background:var(--brown-band)}
.slider{left:31px;top:191px;width:1136px;height:423px;border:8px solid var(--white);border-radius:10px;background:var(--white);overflow:hidden;display:flex}
.slider-photo{width:801px;height:100%;background:
  radial-gradient(ellipse 75% 38% at 40% 48%,rgba(168,88,62,.85),rgba(168,88,62,0) 100%),
  linear-gradient(180deg,#6e6b69 0%,#85807b 35%,#b69a78 68%,#d0b690 100%)}
.slider-panel{flex:1;background:linear-gradient(135deg,#e0b170,#cf9b5a 60%,#d9ab6e);padding:52px 30px 0 38px;color:var(--white)}
.slider-panel h2{font-size:31px;font-weight:600;margin-bottom:16px}
.slider-panel p{font-size:17px;line-height:25px;margin-bottom:10px}
.dots{display:flex;gap:5px;margin-top:30px}
.dots i{width:9px;height:9px;border-radius:50%;background:#f5e8d6}
.dots i:first-child{background:var(--brown-dark)}

.welcome{left:50px;top:694px;width:780px}
.welcome h1{font-size:27px;font-weight:400;color:var(--brown-text);margin-bottom:16px}
.welcome h1 b{font-weight:700}
.welcome p{font-size:13.5px;line-height:22px;color:var(--muted);margin-bottom:10px}
.testimonials{left:864px;top:694px;width:300px}
.testimonials h3{font-size:25px;font-weight:600;color:var(--brown-dark);margin-bottom:14px}
.testimonial-body{position:relative;font-size:13px;line-height:20px;font-style:italic;color:var(--muted)}
.quote-open{position:absolute;left:0;top:-6px;font-size:40px;color:var(--brown-text);font-style:normal;line-height:40px}
.testimonial-photo{float:left;width:92px;height:82px;margin:0 12px 4px 34px;background:linear-gradient(#dcd6cd,#b89077);border:2px solid var(--white);box-shadow:0 0 2px #aaa}
.testimonial-author{font-size:14px;font-weight:700;color:var(--brown-dark);margin:10px 0 0 34px;font-style:normal}
.rule{left:50px;top:946px;width:1100px;border-top:1px dotted #aaa}

.featured-title{left:54px;top:974px;font-size:25px;font-weight:400;color:var(--brown-text)}
.featured-title b{font-weight:700}
.product{position:absolute;width:248px;height:263px;background:var(--cream-card);border-radius:10px;box-shadow:0 1px 4px rgba(0,0,0,.18)}
.product-photo{position:absolute;left:22px;top:28px;width:202px;height:121px;border:2px solid var(--white);box-shadow:0 0 2px #bbb;
  background:
   radial-gradient(ellipse 34% 40% at var(--x,50%) 50%,var(--cup) 0%,var(--cup) 45%,transparent 100%),
   linear-gradient(180deg,var(--wall-tone,var(--wall)) 0%,var(--wall-tone,var(--wall)) 55%,var(--mat) 78%,#cdb594 100%)}
.product-name{position:absolute;left:28px;top:168px;font-size:15px;color:var(--text)}
.product-price{position:absolute;left:28px;top:196px;font-size:23px;color:#333}
.add-cart{position:absolute;left:122px;top:200px;width:96px;height:27px;border-radius:4px;background:var(--brown-btn);color:var(--white);font-size:11px;font-weight:700;text-align:center;line-height:27px}

.footer{left:0;top:2252px;width:1200px;height:358px;background:radial-gradient(ellipse 70% 90% at 45% 40%,var(--wood-light),var(--wood-mid) 60%,var(--wood-deep) 100%)}
.footer-wave{left:0;top:2236px;width:1200px;height:40px}
.footer-col{position:absolute;top:2340px;color:var(--white)}
.footer-col h4{font-size:25px;font-weight:400;margin-bottom:18px}
.footer-col li{list-style:none;font-size:15px;line-height:33px;display:flex;align-items:center;gap:8px}
.footer-col li::before{content:"";width:12px;height:10px;border-radius:0 0 5px 5px;background:#ece4d6}
.map{left:728px;top:2378px;width:322px;height:214px;border:6px solid var(--white);background:linear-gradient(180deg,#c7d8e6,#e3e4cf 50%,#c7d8e6)}
.bottom-bar{left:0;top:2610px;width:1200px;height:147px;background:var(--bottom-bar)}
.copyright{left:52px;top:2694px;font-size:13px;color:#8a7568}
.social{left:996px;top:2686px;display:flex;gap:6px}
.social i{width:34px;height:34px;border-radius:50%;background:var(--white)}
</style>
</head>
<body>
<header class="site-header abs">
  <nav class="util-nav abs"><span>Login</span><span>View Cart</span><span>Check Out</span><span>My Account</span></nav>
  <nav class="main-nav abs"><span>Home</span><span>Categories</span><span>New Arrivals</span><span>About Our Mugs</span><span>Contact</span></nav>
</header>
<div class="brand abs"><div class="brand-mark"></div><div class="brand-name">Cups in Quiet Bloom</div></div>

<section class="hero-band abs"></section>
<section class="slider abs">
  <div class="slider-photo" role="img" aria-label="Three handmade terracotta cups painted with flowers on a woven mat"></div>
  <div class="slider-panel">
    <h2>Hey Coffee lovers!</h2>
    <p>Looking for aunique coffee mug? We offer beautiful handmade coffee mugs and tea cups born in the heart of Europe.</p>
    <p>Beautiful design, precise execu-tion and piece of a heart.</p>
    <div class="dots"><i></i><i></i><i></i><i></i></div>
  </div>
</section>

<section class="welcome abs">
  <h1>Welcome to <b>Cups in Quiet Bloom Mainpage..</b></h1>
  <p>Duis tincidunt lectus quis dui viverra vestibulum. Suspendisse vulputate aliquam dui. Nulla elementum dui ut augue. Aliquam vehicula mi at mauris. Maecenas placerat, nisl at consequat rhoncus, sem nunc gravida justo, quis eleifend arcu velit quis lacus. Morbi magna magna, tincidunt a, mattis non, imperdiet vitae, tellus. Sed odio est, auctor ac, sollicitudin in, consequat vitae, orci. Fusce id felis. Vivamus sollicitudin metus eget eros.</p>
  <p>Mauris vel lacus vitae felis vestibulum volutpat. Etiam est nunc, venenatis in, tristique eu, imperdiet ac, nisl. Cum sociis natoque penatibus et magnis dis parturient montes, nascetur ridiculus mus. In iaculis facilisis massa.</p>
</section>
<aside class="testimonials abs">
  <h3>Testimonials</h3>
  <div class="testimonial-body">
    <span class="quote-open">&ldquo;</span>
    <div class="testimonial-photo" role="img" aria-label="Portrait of the customer"></div>
    Nunc tempus felis vitae urna. Vivamus porttitor, neque at volutpat rutrum, purus nisi eleifend libero Morbi eget arcu. Morbi porta, libero id ullam-corper nonummy, nibh ligula . &rdquo;
    <div class="testimonial-author">By Author Name</div>
  </div>
</aside>
<div class="rule abs"></div>

<h2 class="featured-title abs">Featured <b>Products</b></h2>
<div class="product" style="left:55px;top:1024px"><div class="product-photo" style="--cup:#d98a86" role="img" aria-label="Pink cup with red hearts"></div><div class="product-name">Small tea cup with hearts</div><div class="product-price">$28.00</div><div class="add-cart">ADD TO CART</div></div>
<div class="product" style="left:333px;top:1024px"><div class="product-photo" style="--cup:#c8564a" role="img" aria-label="Red mug with painted lettering"></div><div class="product-name">Small tea cup with hearts</div><div class="product-price">$28.00</div><div class="add-cart">ADD TO CART</div></div>
<div class="product" style="left:610px;top:1024px"><div class="product-photo" style="--cup:#dfe3ea;--wall-tone:#6f6c6b" role="img" aria-label="White mug with blue heart"></div><div class="product-name">Small tea cup with hearts</div><div class="product-price">$28.00</div><div class="add-cart">ADD TO CART</div></div>
<div class="product" style="left:890px;top:1024px"><div class="product-photo" style="--cup:#b77553;--wall-tone:#6c6864" role="img" aria-label="Flowered sugar bowl with lid"></div><div class="product-name">Small tea cup with hearts</div><div class="product-price">$28.00</div><div class="add-cart">ADD TO CART</div></div>

<div class="product" style="left:55px;top:1331px"><div class="product-photo" style="--cup:#e08e84;--x:45%" role="img" aria-label="Pink mug with hearts"></div><div class="product-name">Small tea cup with hearts</div><div class="product-price">$28.00</div><div class="add-cart">ADD TO CART</div></div>
<div class="product" style="left:333px;top:1331px"><div class="product-photo" style="--cup:#c98b5c" role="img" aria-label="Mug with painted red leaf"></div><div class="product-name">Small tea cup with hearts</div><div class="product-price">$28.00</div><div class="add-cart">ADD TO CART</div></div>
<div class="product" style="left:610px;top:1331px"><div class="product-photo" style="--cup:#c0634a;--wall-tone:#7a7470" role="img" aria-label="Terracotta bowl with white flowers"></div><div class="product-name">Small tea cup with hearts</div><div class="product-price">$28.00</div><div class="add-cart">ADD TO CART</div></div>
<div class="product" style="left:890px;top:1331px"><div class="product-photo" style="--cup:#e4e0d4;--wall-tone:#7b7772" role="img" aria-label="White jug with painted figure"></div><div class="product-name">Small tea cup with hearts</div><div class="product-price">$28.00</div><div class="add-cart">ADD TO CART</div></div>

<div class="product" style="left:55px;top:1627px"><div class="product-photo" style="--cup:#8a4a35;--wall-tone:#e9e6e2;--mat:#e2ddd6" role="img" aria-label="Brown mug with dotted pattern"></div><div class="product-name">Small tea cup with hearts</div><div class="product-price">$28.00</div><div class="add-cart">ADD TO CART</div></div>
<div class="product" style="left:333px;top:1627px"><div class="product-photo" style="--cup:#d8c9b4;--wall-tone:#6e6a67" role="img" aria-label="Mug with red stripes"></div><div class="product-name">Small tea cup with hearts</div><div class="product-price">$28.00</div><div class="add-cart">ADD TO CART</div></div>
<div class="product" style="left:610px;top:1627px"><div class="product-photo" style="--cup:#d3b486;--wall-tone:#8ea3be;--mat:#b9c3cf" role="img" aria-label="Close view of a painted mug"></div><div class="product-name">Small tea cup with hearts</div><div class="product-price">$28.00</div><div class="add-cart">ADD TO CART</div></div>
<div class="product" style="left:890px;top:1627px"><div class="product-photo" style="--cup:#c9d3df;--wall-tone:#737170" role="img" aria-label="White mug with blue painting"></div><div class="product-name">Small tea cup with hearts</div><div class="product-price">$28.00</div><div class="add-cart">ADD TO CART</div></div>

<div class="product" style="left:55px;top:1926px"><div class="product-photo" style="--cup:#b5694c;--wall-tone:#7d7773" role="img" aria-label="Terracotta cup with white flowers"></div><div class="product-name">Small tea cup with hearts</div><div class="product-price">$28.00</div><div class="add-cart">ADD TO CART</div></div>
<div class="product" style="left:333px;top:1926px"><div class="product-photo" style="--cup:#a9b9cf;--wall-tone:#6f6c6a" role="img" aria-label="Blue and white mug"></div><div class="product-name">Small tea cup with hearts</div><div class="product-price">$28.00</div><div class="add-cart">ADD TO CART</div></div>
<div class="product" style="left:610px;top:1926px"><div class="product-photo" style="--cup:#c35a44" role="img" aria-label="Red cup with yellow motif"></div><div class="product-name">Small tea cup with hearts</div><div class="product-price">$28.00</div><div class="add-cart">ADD TO CART</div></div>
<div class="product" style="left:890px;top:1926px"><div class="product-photo" style="--cup:#d0584a;--wall-tone:#6c6866" role="img" aria-label="Cup with zigzag pattern"></div><div class="product-name">Small tea cup with hearts</div><div class="product-price">$28.00</div><div class="add-cart">ADD TO CART</div></div>

<footer class="footer abs" role="img" aria-label="Dark wood background"></footer>
<svg class="footer-wave abs" viewBox="0 0 1200 40" preserveAspectRatio="none" aria-hidden="true">
  <path d="M0 0 L1200 0 L1200 6 C900 30 500 -2 0 22 Z" fill="#ffffff"/>
  <path d="M0 22 C500 -2 900 30 1200 6" fill="none" stroke="#e2dccd" stroke-width="4"/>
</svg>
<div class="footer-col" style="left:68px"><h4>Information</h4><ul><li>About Us</li><li>Contact Us</li><li>Privacy Notice</li><li>Shipping &amp; Returns</li><li>Terms of Use</li></ul></div>
<div class="footer-col" style="left:283px"><h4>Online Store</h4><ul><li>View Cart</li><li>Checkout</li><li>Search</li><li>Sitemap</li></ul></div>
<div class="footer-col" style="left:498px"><h4>Support</h4><ul><li>Location</li><li>Contact Us</li><li>FAQ</li><li>Term of Use</li></ul></div>
<div class="footer-col" style="left:720px;top:2332px"><h4>Our Location Map</h4></div>
<div class="map abs" role="img" aria-label="World map showing store locations"></div>

<div class="bottom-bar abs"></div>
<p class="copyright abs">Copyright © 2012 Company Name.&nbsp; All right reserved</p>
<div class="social abs"><i></i><i></i><i></i><i></i></div>
</body>
</html>
```